Wordpress website design for children’s entertainment agency

What is the aim of the website?

The aim for the website is to attract potential bookers and to get them to respond to the Call to action: contact the entertainer - phone call/request a call back/completing a form.
All the information needs to be easy to access and navigate to, especially on mobile view.
The call to action needs to be clear and easy to navigate.

What I need:

Critical - This website needs to look good on all devices.
Easy navigation on a mobile device is essential so the elements need to be bold and easy to click on with a thumb (when in mobile view)

The ‘grid area’ needs to be graphics based with simple descriptions, i.e. ‘magic shows’, Circus Clowns, Face painting, Costume Characters, Party Host, Carnival Parties, Balloon Sculpting, DJ and MC, Princess Parties, Holiday Parties, Fun Add Ons and Contact.

See: http://www.merrylopkin.com/
and http://tottlejoyworks.com/

I would like to see a sample page layout as well to see how your design would be carried through the site layout in the inside pages.

Target Market(s)

The site visitors are mainly mums, aged between 25 - 41. Other visitors will included event organisers looking for entertainment services for baptism, communions and sweet 16’s

Industry/Entity Type

Entertainment Industry

Number of Pages Required

1 page

Font styles to use
Sans Serif

Colors
6c459b
fbed22
0493ce

Requirements
Must have
• Critical - This website needs to look good on all devices.
• Easy navigation on a mobile device is essential so the elements need to be bold and easy to click on with a thumb (when in mobile view)
• The ‘grid area’ needs to be graphics based with simple descriptions, i.e. ‘magic shows’, Circus Clowns, Face painting, Costume Characters, Party Host, Carnival Parties, Balloon Sculpting, DJ and MC, Princess Parties, Holiday Parties, Fun Add Ons and Contact.
• See: http://www.merrylopkin.com/
• and http://tottlejoyworks.com/
Nice to have
• clean looking and fun with an element of ‘Brambo’ and stars (this is the exciting site http://quindlesplaybarn.com/index.html)

```html
<!DOCTYPE html>
<html lang="en">
<head>
<meta charset="utf-8">
<title>Jollyhop Parties – Children's Entertainment</title>
<link href="https://fonts.googleapis.com/css2?family=Open+Sans:wght@400;600;700;800&display=swap" rel="stylesheet">
<style>
:root{
  --purple:#6c459b;
  --purple-dark:#563580;
  --yellow:#fbed22;
  --yellow-dark:#e8d70f;
  --blue:#0493ce;
  --green:#8cc63f;
  --green-light:#b5dd6a;
  --ink:#333;
  --muted:#888;
  --line:#e3e3e3;
  --footer:#1e1f29;
  --footer-bar:#14151c;
}
*{box-sizing:border-box;margin:0;padding:0}
html,body{width:1200px;height:2568px;overflow:hidden}
body{font-family:"Open Sans",Arial,sans-serif;color:var(--ink);position:relative}
.backdrop{position:absolute;inset:0;background:radial-gradient(circle at 50% 40%,var(--green-light),var(--green) 70%)}
.page{position:absolute;left:108px;top:0;width:984px;height:2560px;background:#fff}
.abs{position:absolute}

/* header */
.brand{left:22px;top:24px;display:flex;align-items:center;gap:12px}
.brand-mark{width:60px;height:60px;border-radius:50%;background:var(--purple)}
.brand-name{font-size:30px;font-weight:800;color:var(--purple)}
.phone{right:24px;top:82px;font-size:26px;font-weight:600;color:#555;display:flex;align-items:center;gap:10px}
.phone-dot{width:30px;height:30px;border-radius:50%;background:#3bbf4a}
.social{right:176px;top:140px;display:flex;gap:6px}
.social span{width:34px;height:34px;display:block;background:var(--purple);border-radius:3px}
.btn{display:inline-block;color:#fff;font-weight:700;font-size:15px;text-align:center;border-radius:3px}
.contact-top{right:24px;top:140px;width:138px;height:36px;line-height:36px;background:var(--blue);font-size:14px}

/* nav */
.nav{left:0;top:208px;width:984px;height:40px;background:var(--yellow);display:flex;padding-left:20px}
.nav a{font-size:13px;font-weight:700;color:#444;text-decoration:none;padding:0 28px;line-height:40px}
.nav a.active{background:var(--yellow-dark)}

/* slider */
.slider{left:0;top:260px;width:984px;height:510px;background:linear-gradient(120deg,#c33b2a,#e58a3a 35%,#7a3a8f 70%,#3a244f)}
.arrow{width:36px;height:36px;border-radius:50%;background:rgba(0,0,0,.45);top:497px}
.caption{left:120px;top:612px;width:440px;height:128px;background:rgba(30,20,50,.78);padding:16px 20px;color:#fff}
.caption p{font-size:19px;line-height:26px}
.caption .btn{height:30px;line-height:30px;padding:0 18px;font-size:13px;margin-top:8px;margin-right:8px}
.b-blue{background:var(--blue)}.b-purple{background:var(--purple)}

/* grid */
.grid{left:20px;top:812px;width:664px;display:grid;grid-template-columns:repeat(3,1fr);gap:8px 14px}
.tile-img{height:150px;display:block}
.tile-label{height:32px;line-height:32px;text-align:center;font-size:14px;font-weight:700;text-transform:uppercase;color:#333}
.tile-label.on{background:var(--purple);color:#fff}

/* contact form */
.contact-box{left:704px;top:812px;width:260px;height:390px;background:var(--purple);padding:18px 16px;color:#fff}
.contact-box h3{font-size:20px;font-weight:700;text-align:center;padding-bottom:10px;border-bottom:1px solid rgba(255,255,255,.35);margin-bottom:14px}
.contact-box label{display:block;font-size:11px;font-weight:700;margin-bottom:4px}
.field{background:#8a66b5;height:30px;margin-bottom:14px}
.field.tall{height:84px}
.submit{width:100%;height:40px;line-height:40px;background:var(--blue);font-size:20px}

/* side */
.side-title{font-size:24px;color:#444;font-weight:600}
.feeds{left:704px;top:1250px;width:260px}
.feed{display:flex;gap:8px;margin-top:14px}
.feed-icon{width:14px;height:14px;background:var(--blue);border-radius:50%;flex:none;margin-top:2px}
.feed p{font-size:11px;line-height:15px;color:#666}
.feed small{display:block;font-size:10px;color:var(--blue);margin-top:4px}
.news{left:704px;top:1620px;width:260px}
.news-item{display:flex;gap:12px;margin-top:18px}
.news-thumb{width:64px;height:64px;flex:none}
.news-item h4{font-size:13px;color:#555;font-weight:600}
.news-item p{font-size:11px;color:#888;line-height:15px}
.news-item small{font-size:10px;color:var(--blue)}

/* about */
.about-img{left:20px;top:1640px;width:230px;height:330px;background:linear-gradient(160deg,#e23b3b,#3a5fb0 60%,#f3c23a)}
.about{left:270px;top:1640px;width:414px}
.about h2{font-size:30px;font-weight:600;color:#444;margin-bottom:14px}
.about p{font-size:13px;line-height:21px;color:#777}
.about .btn{height:34px;line-height:34px;padding:0 20px;font-size:13px;margin-top:22px;margin-right:10px}

/* footer */
.footer{left:0;top:2040px;width:984px;height:472px;background:var(--footer);color:#fff}
.footer-img{left:0;top:60px;width:250px;height:360px;background:radial-gradient(circle at 50% 55%,#3a3a55,#1e1f29 70%)}
.footer h3{font-size:20px;font-weight:700;letter-spacing:.5px}
.map{left:340px;top:90px;width:200px;height:130px;background:linear-gradient(135deg,#e9ecef,#cfd8d3)}
.foot-phone{left:340px;top:236px;font-size:16px;display:flex;align-items:center;gap:8px}
.qc{left:690px;top:40px;width:270px}
.qc .field{background:#2c2d3a;border:1px solid #3b3c4a;height:30px;margin-bottom:10px;font-size:11px;color:#999;padding-left:8px;line-height:28px}
.qc .field.tall{height:110px}
.send{width:100%;height:36px;line-height:36px;background:var(--blue);font-size:15px}
.bottom-bar{left:0;top:2512px;width:984px;height:48px;background:var(--footer-bar);color:#888;font-size:11px;display:flex;align-items:center;justify-content:space-between;padding:0 22px}
.bottom-bar nav span{margin-left:14px}
</style>
</head>
<body>
<div class="backdrop" role="img" aria-label="Bright green backdrop scattered with white stars"></div>

<div class="page">
  <header>
    <div class="abs brand"><span class="brand-mark"></span><span class="brand-name">Jollyhop Parties</span></div>
    <div class="abs phone">+38 555 0142 <span class="phone-dot"></span></div>
    <div class="abs social">
      <span></span><span></span><span></span><span></span>
    </div>
    <a class="abs btn contact-top">CONTACT US</a>
  </header>

  <nav class="abs nav">
    <a class="active">HOME</a><a>ABOUT</a><a>FREQ CONTENT</a><a>VIDEOS</a><a>TESTIMONIALS</a><a>CONTACT</a><a>FUN STOP</a>
  </nav>

  <section>
    <div class="abs slider" role="img" aria-label="Photo of laughing children dressed up in party costumes"></div>
    <svg class="abs arrow" style="left:16px" viewBox="0 0 36 36"><path d="M21 11l-7 7 7 7" stroke="#fff" stroke-width="3" fill="none"/></svg>
    <svg class="abs arrow" style="right:16px" viewBox="0 0 36 36"><path d="M15 11l7 7-7 7" stroke="#fff" stroke-width="3" fill="none"/></svg>
    <div class="abs caption">
      <p>Aenean eu enim mi. Suspendisse potenti. Aliquam erat volutpat. Mauris eu elementum urna</p>
      <a class="btn b-blue">Call Now</a><a class="btn b-purple">Read More</a>
    </div>
  </section>

  <section class="abs grid">
    <div><span class="tile-img" role="img" aria-label="Magician performing a trick" style="background:linear-gradient(135deg,#2b2340,#7a5aa8)"></span><div class="tile-label">Magic Shows</div></div>
    <div><span class="tile-img" role="img" aria-label="Circus clown in colourful costume" style="background:linear-gradient(135deg,#4a6fb5,#e24b4b)"></span><div class="tile-label on">Circus Clowns</div></div>
    <div><span class="tile-img" role="img" aria-label="Child with painted face" style="background:linear-gradient(135deg,#e9a94a,#b0453a)"></span><div class="tile-label">Face Painting</div></div>
    <div><span class="tile-img" role="img" aria-label="Costume character at a party" style="background:linear-gradient(135deg,#d9c7a5,#6f8fb8)"></span><div class="tile-label">Costume Characters</div></div>
    <div><span class="tile-img" role="img" aria-label="Party host with children" style="background:linear-gradient(135deg,#8aa0b8,#d5c6b0)"></span><div class="tile-label">Party Host</div></div>
    <div><span class="tile-img" role="img" aria-label="Carnival party with masks" style="background:linear-gradient(135deg,#c03a3a,#3a2a5a)"></span><div class="tile-label">Carnival Parties</div></div>
    <div><span class="tile-img" role="img" aria-label="Balloon sculptures" style="background:linear-gradient(135deg,#f1d04a,#e25b8a)"></span><div class="tile-label">Balloon Sculpting</div></div>
    <div><span class="tile-img" role="img" aria-label="DJ lights at a party" style="background:linear-gradient(135deg,#1e2a6a,#3aa0d8)"></span><div class="tile-label">DJ and MC</div></div>
    <div><span class="tile-img" role="img" aria-label="Princess party with cake" style="background:linear-gradient(135deg,#f3c6d6,#b88ac8)"></span><div class="tile-label">Princess Parties</div></div>
    <div><span class="tile-img" role="img" aria-label="Holiday party celebration" style="background:linear-gradient(135deg,#7a2a3a,#d88a3a)"></span><div class="tile-label">Holiday Parties</div></div>
    <div><span class="tile-img" role="img" aria-label="Fun party add ons" style="background:linear-gradient(135deg,#3a8ac8,#f0a83a)"></span><div class="tile-label">Fun Add Ons</div></div>
    <div><span class="tile-img" role="img" aria-label="Telephone on a desk" style="background:linear-gradient(135deg,#c8c8c8,#6a6a6a)"></span><div class="tile-label">Contact</div></div>
  </section>

  <aside class="abs contact-box">
    <h3>CONTACT</h3>
    <label>NAME</label><div class="field"></div>
    <label>EMAIL</label><div class="field"></div>
    <label>MESSAGE</label><div class="field tall"></div>
    <a class="btn submit">SUBMIT</a>
  </aside>

  <aside class="abs feeds">
    <h3 class="side-title">Social Feeds</h3>
    <div class="feed"><span class="feed-icon"></span><p>Book our clowns for your next birthday party and watch the fun begin today.<small>2 hours ago · Reply · Share</small></p></div>
    <div class="feed"><span class="feed-icon"></span><p>New princess party packages are now open for spring bookings this year.<small>5 hours ago · Reply · Share</small></p></div>
    <div class="feed"><span class="feed-icon"></span><p>Thanks to every family who joined our magic show at the weekend.<small>1 day ago · Reply · Share</small></p></div>
  </aside>

  <aside class="abs news">
    <h3 class="side-title">Latest News</h3>
    <div class="news-item"><span class="news-thumb" role="img" aria-label="Party news photo" style="background:linear-gradient(135deg,#9a8a7a,#4a3a3a)"></span><div><h4>Slots still open</h4><p>Summer party dates are filling fast, call now.</p><small>22 December 2015</small></div></div>
    <div class="news-item"><span class="news-thumb" role="img" aria-label="Party news photo" style="background:linear-gradient(135deg,#c03a3a,#3a1a2a)"></span><div><h4>Festive specials</h4><p>Holiday shows for schools and family events.</p><small>18 December 2015</small></div></div>
  </aside>

  <section>
    <div class="abs about-img" role="img" aria-label="Illustration of a ringmaster entertainer in red coat and top hat"></div>
    <div class="abs about">
      <h2>About The Entertainer</h2>
      <p>Our entertainers bring laughter, magic and games to every party. From little ones to teenagers, we plan shows that fit your day, your venue and your budget. Each host is friendly, trained and fully checked, so parents can relax and enjoy the party too. We cover birthdays, baptisms, communions, sweet sixteens and school fairs, with balloon art, face painting and music to keep every guest smiling from start to finish. Get in touch and we will help you pick the perfect show.</p>
      <a class="btn b-blue">Read More</a><a class="btn b-purple">Contact the entertainer</a>
    </div>
  </section>

  <footer class="abs footer">
    <div class="abs footer-img" role="img" aria-label="Magic top hat with sparkling stars"></div>
    <h3 class="abs" style="left:340px;top:40px">FIND US</h3>
    <div class="abs map" role="img" aria-label="Location map"></div>
    <div class="abs foot-phone">
      <svg width="18" height="18" viewBox="0 0 24 24"><path fill="#fff" d="M6.6 10.8c1.4 2.8 3.8 5.1 6.6 6.6l2.2-2.2c.3-.3.7-.4 1-.2 1.1.4 2.3.6 3.6.6.6 0 1 .4 1 1V20c0 .6-.4 1-1 1C10.6 21 3 13.4 3 4c0-.6.4-1 1-1h3.5c.6 0 1 .4 1 1 0 1.3.2 2.5.6 3.6.1.3 0 .7-.2 1z"/></svg>
      +39 555 0187
    </div>
    <div class="abs qc">
      <h3 style="margin-bottom:22px">QUICK CONTACT US</h3>
      <div class="field">Name</div>
      <div class="field">Email Address</div>
      <div class="field tall">Message</div>
      <a class="btn send">SEND IT NOW</a>
    </div>
  </footer>
  <div class="abs bottom-bar">
    <span>Copyright 2015 Jollyhop Parties · Privacy Policy · Terms &amp; Conditions</span>
    <nav><span>Home</span><span>About</span><span>Party Guides</span><span>Videos</span><span>Testimonials</span><span>Contact</span><span>Fun Stop</span></nav>
  </div>
</div>
</body>
</html>
```